Business Card Design Project

New Business Card design for Varodine Technology Ltd using new Logo and new Tagline for staffing company.

About us from our website - www.varodine.example:

VaroDine is a leading and recognized Electronic Entertainment, Workforce Augmentation, and Project Management solutions provider with clients in Electronic Entertainment, Legal, Technology, Government and other verticals that range in size from start up organizations to Zenlar 500 companies. VaroDine is certified as an 8(a) minority and woman owned enterprise, established in 1998.

Target Market(s)

Companies in Electronic Entertainment, Legal, Government and Technology

Industry/Entity Type

Business

Requirements
Must have
• Must include in small letters the following information on back:

Established in 1998
8(a)(w)(e), Cage #7KRT9, DUNS #462137580

Front should have the following:
Derek Holloway
Vice President
5820 Birchmont Road
Fallowby, FB 482917
555-318-2746 X 100
555-902-6613 Fax
555-318-2746 Toll Free
name@varodine.example

Our Tagline: Connect • Collaborate • Achieve

```html
<!DOCTYPE html>
<html lang="en">
<head>
<meta charset="utf-8">
<title>VaroDine Business Card</title>
<link href="https://fonts.googleapis.com/css2?family=Arimo:wght@400;700&family=Great+Vibes&display=swap" rel="stylesheet">
<style>
  :root {
    --page-bg: #ffffff;
    --navy: #0d2f78;
    --navy-deep: #08215c;
    --royal: #1456b8;
    --sky: #3a8fe0;
    --glow: #8fd0ff;
    --swoosh: #4fa6ff;
    --white: #ffffff;
    --soft-white: rgba(255, 255, 255, 0.85);
  }
  * { box-sizing: border-box; margin: 0; padding: 0; }
  html, body { width: 880px; height: 1200px; overflow: hidden; background: var(--page-bg); }
  .canvas { position: relative; width: 880px; height: 1200px; }

  .card {
    position: absolute;
    left: 30px;
    width: 820px;
    height: 550px;
    overflow: hidden;
    box-shadow: 0 4px 10px rgba(0, 0, 0, 0.35);
    font-family: "Arimo", Arial, sans-serif;
    color: var(--white);
  }
  .card--front { top: 30px; background: linear-gradient(160deg, var(--royal) 0%, var(--sky) 55%, var(--royal) 100%); }
  .card--back { top: 620px; background: linear-gradient(170deg, var(--navy) 0%, var(--royal) 45%, var(--sky) 100%); }

  .light-burst {
    position: absolute;
    inset: 0;
    background:
      radial-gradient(circle at 78% 22%, rgba(200, 235, 255, 0.75) 0%, rgba(143, 208, 255, 0.35) 18%, rgba(143, 208, 255, 0) 45%),
      radial-gradient(circle at 88% 85%, rgba(143, 208, 255, 0.35) 0%, rgba(143, 208, 255, 0) 35%);
  }
  .card--back .light-burst {
    background:
      radial-gradient(circle at 92% 10%, rgba(200, 235, 255, 0.7) 0%, rgba(143, 208, 255, 0.3) 20%, rgba(143, 208, 255, 0) 48%),
      radial-gradient(circle at 80% 90%, rgba(143, 208, 255, 0.4) 0%, rgba(143, 208, 255, 0) 35%);
  }

  .side-panel { position: absolute; inset: 0; width: 820px; height: 550px; }

  .brand-name {
    position: absolute;
    font-weight: 700;
    color: var(--white);
    letter-spacing: -1px;
  }
  .card--front .brand-name { left: 34px; top: 88px; font-size: 48px; }
  .card--back .brand-name { left: 0; right: 0; top: 160px; text-align: center; font-size: 82px; line-height: 1.1; }

  .person-name {
    position: absolute;
    right: 36px;
    top: 22px;
    font-family: "Great Vibes", cursive;
    font-weight: 400;
    font-size: 64px;
    line-height: 1;
  }
  .person-title {
    position: absolute;
    right: 48px;
    top: 92px;
    font-size: 21px;
    font-weight: 700;
  }

  .contact-list {
    position: absolute;
    right: 20px;
    top: 300px;
    list-style: none;
    text-align: right;
    font-size: 21px;
    font-weight: 700;
    line-height: 34px;
  }

  .tagline {
    position: absolute;
    left: 40px;
    right: 40px;
    top: 266px;
    text-align: center;
    font-size: 26px;
    font-weight: 700;
    letter-spacing: 1px;
  }
  .market {
    position: absolute;
    left: 40px;
    right: 40px;
    top: 330px;
    text-align: center;
    font-size: 31px;
    font-weight: 700;
    line-height: 38px;
  }
  .credentials {
    position: absolute;
    left: 40px;
    right: 40px;
    top: 470px;
    text-align: center;
    font-size: 16px;
    font-weight: 400;
    line-height: 22px;
    color: var(--soft-white);
  }
</style>
</head>
<body>
<main class="canvas">

  <section class="card card--front" aria-label="Card front">
    <div class="light-burst" role="img" aria-label="Radiating light rays and soft bokeh bubbles"></div>
    <svg class="side-panel" viewBox="0 0 820 550" aria-hidden="true">
      <path d="M0 0 H300 C230 120 200 260 0 400 Z" fill="var(--navy-deep)"/>
      <path d="M0 400 C200 260 230 120 300 0 H330 C250 140 230 300 0 430 Z" fill="var(--navy)"/>
      <path d="M300 0 C230 120 200 260 0 400" fill="none" stroke="var(--swoosh)" stroke-width="4"/>
      <path d="M0 550 C180 470 260 320 280 250" fill="none" stroke="var(--glow)" stroke-width="2" opacity="0.6"/>
    </svg>
    <div class="brand-name">VaroDine</div>
    <h1 class="person-name">Derek Holloway</h1>
    <p class="person-title">Vice President</p>
    <ul class="contact-list">
      <li>5820 Birchmont Road</li>
      <li>Fallowby, FB 482917</li>
      <li>555-318-2746 X 100</li>
      <li>555-902-6613 Fax</li>
      <li>555-318-2746 Toll Free</li>
      <li>name@varodine.example</li>
    </ul>
  </section>

  <section class="card card--back" aria-label="Card back">
    <div class="light-burst" role="img" aria-label="Radiating light rays and soft bokeh bubbles"></div>
    <div class="brand-name">VaroDine</div>
    <p class="tagline">Connect • Collaborate • Achieve</p>
    <p class="market">Companies in Electronic Entertainment, Legal,<br>Government and Technology</p>
    <p class="credentials">Established in 1998<br>8(a)(w)(e), Cage #7KRT9, DUNS #462137580</p>
  </section>

</main>
</body>
</html>
```